Firm of surveyors needs a professional yet friendly looking flyer

Our company offers help to landlords who have a phone mast on their property. We help them to negotiate the best rent and lease terms. There are so many landlords who don't seek professional advice because they don't know it's available. We want to send them a flyer which is informative, looks professional but also friendly so it prompts them to call us. I have attached the wording and some pictures but have more I can send but they were too large to attach.

Target Market(s)

Ranges from farmers to large corporations and land owners

Industry/Entity Type

Surveyor

Font styles to use
Sans Serif

Colors
acd136
9bcb3c
000000
ffffff
606060
848484

Requirements
Must have
• Must be clear, must give a professional look, must include pictures, must include our logo, must use our colour scheme (or variations of it). Ideally, I would like a try-fold design if possible.
Nice to have
• I would like there to be stand out lines to catch the readers eye (I have included some on the wording document). I would like a clean and modern design
Should not have
• Should not be too fussy

```html
<!DOCTYPE html>
<html lang="en">
<head>
<meta charset="utf-8">
<title>The Signal Site Company – Trifold Flyer</title>
<link href="https://fonts.googleapis.com/css2?family=Cabin:wght@400;500;600;700&family=Roboto+Condensed:ital,wght@0,400;0,700;1,400;1,700&display=swap" rel="stylesheet">
<style>
  :root{
    --green:#6fa51f;
    --green-light:#9bcb3c;
    --green-bright:#acd136;
    --green-dark:#4a7a12;
    --blue-deep:#2f5fae;
    --blue-mid:#4f82cc;
    --blue-sky:#7fb0e6;
    --ink:#1f1f1f;
    --grey:#606060;
    --grey-light:#848484;
    --white:#ffffff;
    --stage:#ffffff;
  }
  *{box-sizing:border-box;margin:0;padding:0}
  html,body{width:1200px;height:1200px;overflow:hidden;background:var(--stage)}
  .flyer{position:absolute;left:30px;top:194px;width:1140px;height:812px;display:flex;background:var(--white);
    box-shadow:0 2px 10px rgba(0,0,0,.25);font-family:"Cabin",sans-serif}
  .panel{position:relative;height:100%;overflow:hidden}

  /* Panel 1 – services */
  .panel-services{width:386px;background:linear-gradient(180deg,var(--blue-deep) 0%,var(--blue-mid) 45%,var(--blue-sky) 100%);color:var(--white)}
  .panel-services .photo-mast{position:absolute;left:0;right:0;top:270px;bottom:0;
    background:linear-gradient(180deg,rgba(255,255,255,0) 0%,rgba(210,220,235,.35) 60%,#c9ced6 100%)}
  .lead-quote{position:absolute;left:30px;top:22px;width:340px;font-family:"Roboto Condensed",sans-serif;
    font-style:italic;font-size:20px;line-height:25px}
  .services-title{position:absolute;left:0;width:334px;top:88px;text-align:center;font-weight:700;font-size:21px;color:var(--green-bright)}
  .services-list{position:absolute;top:142px;left:26px;display:flex}
  .services-list ul{list-style:none;font-size:11.6px;font-weight:600;line-height:15.8px}
  .services-list ul:first-child{width:170px;padding-right:10px;border-right:1px solid rgba(255,255,255,.7)}
  .services-list ul:last-child{padding-left:10px;width:175px}
  .services-list li{position:relative;padding-left:16px}
  .services-list li::before{content:"";position:absolute;left:2px;top:5px;width:6px;height:6px;border-radius:50%;background:var(--green-bright)}

  /* Panel 2 – contact */
  .panel-contact{width:376px;background:var(--white);text-align:center}
  .photo-meeting{position:absolute;left:0;top:0;width:100%;height:171px;background:linear-gradient(135deg,#e8e4df,#c9b8a8 45%,#4a4f5c)}
  .photo-couple{position:absolute;left:0;bottom:0;width:100%;height:300px;
    background:linear-gradient(180deg,rgba(255,255,255,1) 0%,#f1ebe6 30%,#e9d7cc 65%,#d8c3b4 100%)}
  .contact-prompt{position:absolute;top:206px;width:100%;font-family:"Roboto Condensed",sans-serif;font-style:italic;font-size:16px;color:var(--grey)}
  .contact-cta{position:absolute;top:234px;width:100%;color:var(--green);font-size:24px;line-height:30px;font-weight:500}
  .contact-cta .upper{display:block}
  .contact-rule{position:absolute;top:301px;left:98px;width:170px;height:1px;background:#b5b5b5}
  .company-name{position:absolute;top:320px;width:100%;font-weight:700;font-size:16px;color:var(--green-dark)}
  .contact-lines{position:absolute;top:345px;width:100%;list-style:none;font-size:13.4px;line-height:18.6px;color:var(--ink)}
  .contact-lines svg{width:11px;height:11px;vertical-align:-1px;margin-right:5px;fill:var(--green-dark)}
  .contact-lines .address{margin-top:3px;line-height:16px}

  /* Panel 3 – cover */
  .panel-cover{width:378px;background:var(--white)}
  .brand{position:absolute;top:80px;left:0;width:100%;display:flex;justify-content:center;align-items:center;gap:10px}
  .brand-dot{width:16px;height:16px;border-radius:50%;background:var(--green)}
  .brand-name{font-family:"Cabin",sans-serif;font-weight:700;font-size:22px;color:var(--green-dark);letter-spacing:.2px}
  .cover-bands{position:absolute;left:0;top:170px;width:100%;height:460px}
  .photo-tower{position:absolute;left:0;top:181px;width:100%;height:432px;
    background:linear-gradient(180deg,#5d93d8 0%,#a9cbee 45%,#dbe8f4 68%,#7ea24a 72%,#5d8a2c 100%)}
  .cover-kicker{position:absolute;top:650px;width:100%;text-align:center;font-family:"Roboto Condensed",sans-serif;font-size:20px;color:var(--ink);letter-spacing:.2px}
  .cover-headline{position:absolute;top:670px;width:100%;text-align:center;font-family:"Roboto Condensed",sans-serif;font-weight:700;font-size:35px;color:var(--green-dark);letter-spacing:.5px}
  .cover-band{position:absolute;left:0;top:727px;width:100%;height:61px;background:var(--green);color:var(--white);
    font-family:"Roboto Condensed",sans-serif;font-style:italic;font-size:20px;line-height:24px;text-align:center;padding-top:6px}
</style>
</head>
<body>
<main class="flyer">

  <section class="panel panel-services">
    <div class="photo-mast" role="img" aria-label="Photograph of a rooftop phone mast with antennas against a blue sky"></div>
    <p class="lead-quote">Landlords should not sign anything until they have sought professional advice</p>
    <h2 class="services-title">OUR SERVICES</h2>
    <div class="services-list">
      <ul>
        <li>Rent Reviews</li>
        <li>Lease Renewals</li>
        <li>Network Consolidation Issues</li>
        <li>Site Shares</li>
        <li>Rent Protection</li>
        <li>Equipment Upgrades</li>
      </ul>
      <ul>
        <li>Mast Removals / Decommissioning</li>
        <li>Mast Sales and Marketing</li>
        <li>Land Marketing for Masts</li>
        <li>Mast Management and Portfolios</li>
        <li>Safety Testing</li>
      </ul>
    </div>
  </section>

  <section class="panel panel-contact">
    <div class="photo-meeting" role="img" aria-label="Photograph of a young couple shaking hands with an advisor in a suit"></div>
    <p class="contact-prompt">Unsure whether you are getting the best rent?</p>
    <p class="contact-cta"><span class="upper">CALL US NOW FOR A FREE</span>no obligation chat</p>
    <div class="contact-rule"></div>
    <h3 class="company-name">The Signal Site Company Ltd</h3>
    <ul class="contact-lines">
      <li><svg viewBox="0 0 12 12"><path d="M2.5 1l2 2-1 1.5c.6 1.4 1.6 2.4 3 3L8 6.5l2 2-1.2 1.8C5 10 2 7 1.7 2.2z"/></svg>01632 960543</li>
      <li><svg viewBox="0 0 12 12"><rect x="1" y="3" width="10" height="3" rx="1"/><rect x="3" y="6" width="6" height="5"/></svg>01632 960222</li>
      <li><svg viewBox="0 0 12 12"><path d="M1 3h10v6H1z M1 3l5 3.5L11 3" fill="none" stroke="#4a7a12" stroke-width="1.4"/></svg>hello@signalsiteco.co.uk</li>
      <li><svg viewBox="0 0 12 12"><circle cx="6" cy="6" r="5" fill="none" stroke="#4a7a12" stroke-width="1.4"/><path d="M1 6h10M6 1v10" stroke="#4a7a12" stroke-width="1"/></svg>www.signalsiteco.co.uk</li>
      <li class="address"><svg viewBox="0 0 12 12"><path d="M6 0.5a4 4 0 0 1 4 4c0 3-4 7-4 7s-4-4-4-7a4 4 0 0 1 4-4zm0 2.5a1.5 1.5 0 1 0 0 3 1.5 1.5 0 0 0 0-3z"/></svg>The Mill Offices,<br>Riverside Business Park,<br>Oakford, Shropshire, SY99 1ZZ</li>
    </ul>
    <div class="photo-couple" role="img" aria-label="Photograph of a senior couple smiling while reading paperwork together"></div>
  </section>

  <section class="panel panel-cover">
    <div class="brand">
      <span class="brand-dot"></span>
      <span class="brand-name">THE SIGNAL SITE COMPANY</span>
    </div>
    <svg class="cover-bands" viewBox="0 0 378 460" preserveAspectRatio="none" aria-hidden="true">
      <polygon points="0,0 270,0 264,11 0,11" fill="var(--green)"/>
      <polygon points="135,446 378,446 378,460 130,460" fill="#c4c4c4"/>
    </svg>
    <div class="photo-tower" role="img" aria-label="Photograph of a lattice phone mast on a green hillside under a blue sky"></div>
    <p class="cover-kicker">OUR EXPERT SURVEYORS WILL BE</p>
    <h1 class="cover-headline">HAPPY TO HELP YOU</h1>
    <p class="cover-band">Understand proposed changes<br>&amp; what they could mean for you</p>
  </section>

</main>
</body>
</html>
```